Double-sided Business card design needed

I work as an independent consultant in a range of fields, and I need a business card to describes the two main business operations in a two-sided format:

(1) KILT - Kinship Inclusion Learning Therapy

(2) PORT - Promoting Original Regional Tribes

My personal profile so far has been describing myself as:
Dr Gavin Thorpe- Independent R&D Consultant in Community Wellbeing, Education, Mental Health and Disability Support Reform

Industry/Entity Type

Business

Contact Information for Business Card

I need a double-sided business card, describing two different but related businesses that I operate: one in Disability & Mental Health, Education and Community Wellbeing consulting, teaching and research; the other in Indigenous/First Nations-specific community cultural development

Logo Text

See the two business names below for logo text - and they need two different logo designs

Logo styles of interest
Pictorial/Combination Logo

```html
<!DOCTYPE html>
<html lang="en">
<head>
<meta charset="utf-8">
<title>Dr Gavin Thorpe – Double-sided Business Card</title>
<link rel="stylesheet" href="https://fonts.googleapis.com/css2?family=Michroma&family=Roboto+Condensed:wght@400&display=swap">
<style>
  :root {
    --backdrop: #8e8f96;
    --paper-cream: #f1eedb;
    --paper-grey: #e4e4ea;
    --band-green: #0d7a4e;
    --band-purple: #3b3597;
    --accent-red: #c6302c;
    --mark-grey: #4f4f52;
    --band-text: #ffffff;
  }
  * { box-sizing: border-box; margin: 0; padding: 0; }
  html, body { width: 1200px; height: 800px; overflow: hidden; }
  body {
    background: var(--backdrop);
    position: relative;
  }
  .card {
    position: absolute;
    width: 520px;
    height: 300px;
    box-shadow: 0 6px 18px rgba(0,0,0,0.25);
    overflow: hidden;
  }
  .card--kilt { left: 70px; top: 90px; background: var(--paper-cream); }
  .card--port { left: 610px; top: 410px; background: var(--paper-grey); }

  .band-top {
    position: absolute; left: 0; top: 0; width: 100%; height: 32px;
    display: flex; align-items: center; justify-content: center;
    font-family: "Michroma", sans-serif;
    font-variant: small-caps;
    font-size: 12px; letter-spacing: 1.2px;
    color: var(--band-text);
  }
  .card--kilt .band-top { background: var(--band-green); }
  .card--port .band-top { background: var(--band-purple); }

  .band-bottom {
    position: absolute; left: 0; bottom: 0; width: 100%;
    color: var(--band-text);
    font-family: "Roboto Condensed", sans-serif;
  }
  .card--kilt .band-bottom {
    height: 60px; background: var(--band-green);
    display: flex; align-items: center; justify-content: center;
    text-align: center; font-size: 14.5px; line-height: 1.35;
  }
  .card--port .band-bottom {
    height: 68px; background: var(--band-purple);
    display: flex; align-items: center; justify-content: space-between;
    padding: 0 36px 0 36px; font-size: 17px;
  }
  .contact { display: flex; align-items: center; gap: 8px; }
  .contact svg { width: 20px; height: 20px; }

  .identity {
    position: absolute; left: 0; top: 32px; width: 100%;
    display: flex; align-items: center;
  }
  .card--kilt .identity { height: 208px; }
  .card--port .identity { height: 200px; }

  .logo {
    width: 150px;
    display: flex; flex-direction: column; align-items: center; gap: 12px;
    padding-left: 14px;
  }
  .logo-dot {
    width: 36px; height: 36px; border-radius: 50%;
    background: var(--accent-red);
  }
  .logo-name {
    font-family: "Michroma", sans-serif;
    font-size: 24px; letter-spacing: 2px;
    color: var(--mark-grey);
  }
  .divider { width: 2px; height: 104px; margin: 0 34px 0 10px; }
  .card--kilt .divider { background: var(--band-green); }
  .card--port .divider { background: var(--band-purple); }

  .holder-name {
    font-family: "Michroma", sans-serif;
    font-variant: small-caps;
    font-size: 21px; letter-spacing: 2.5px;
    color: var(--accent-red);
    white-space: nowrap;
  }
</style>
</head>
<body>

<section class="card card--kilt" aria-label="Business card, Kinship Inclusion Learning Therapy side">
  <div class="band-top">Kinship Inclusion Learning Therapy</div>
  <div class="identity">
    <div class="logo">
      <span class="logo-dot"></span>
      <span class="logo-name">KILT</span>
    </div>
    <span class="divider"></span>
    <p class="holder-name">Dr Gavin Thorpe</p>
  </div>
  <div class="band-bottom">
    <p>Independent R&amp;D Consultant in Community Wellbeing, Education,<br>Mental Health and Disability Support Reform</p>
  </div>
</section>

<section class="card card--port" aria-label="Business card, Promoting Original Regional Tribes side">
  <div class="band-top">Promoting Original Regional Tribes</div>
  <div class="identity">
    <div class="logo">
      <span class="logo-dot"></span>
      <span class="logo-name">PORT</span>
    </div>
    <span class="divider"></span>
    <p class="holder-name">Dr Gavin Thorpe</p>
  </div>
  <div class="band-bottom">
    <p class="contact">
      <svg viewBox="0 0 24 24" aria-hidden="true"><path fill="#1a1a1a" d="M6.6 2.5c.6-.3 1.3-.1 1.6.5l1.8 3.4c.3.6.1 1.2-.4 1.6L8.2 9c.9 2.5 2.9 4.6 5.4 5.6l1.1-1.4c.4-.5 1.1-.7 1.6-.4l3.4 1.8c.6.3.8 1 .5 1.6l-1 2.2c-.4.8-1.2 1.3-2.1 1.2C9.9 19 4.9 14 4.3 6.9c-.1-.9.4-1.7 1.2-2.1z"/></svg>
      01 98765432
    </p>
    <p class="contact">
      <svg viewBox="0 0 24 24" aria-hidden="true"><g fill="none" stroke="#1a1a1a" stroke-width="1.8" stroke-linejoin="round"><path d="M3 10l9-6 9 6v10H3z"/><path d="M3 10l9 6 9-6"/></g></svg>
      hello@thorpeconsult.net
    </p>
  </div>
</section>

</body>
</html>
```